PRISM Marketing Campaign Schools 2025

We are seeking a professional, eye-catching, double-sided A4 flyer to promote our PRISM LED video walls to primary and secondary schools across Victoria. The flyer should communicate the benefits of our product in a clear and engaging way, targeting school decision-makers, and encourage immediate action. Full design brief is in the attachments.

Target Market(s)

School decision makers and buyers, school Principals and school business managers

Industry/Entity Type

Audio Visual products to schools for teaching and student engagement

Colors
EB3D1F
EC4F4E
F09395
F8D3D4
FCEDEE

Requirements
Must have
• Content to Include: • PRISM LED video wall logo • Show that we are located in Melbourne, Sydney, Brisbane, Perth • Website: www.tornelascreens.com.au • Strong call-to-action: Free on-site demonstration at your school
Nice to have
• Design Style: • Bright, modern, and professional. • Appealing to school administrators and teachers. • Visually highlight the product (images of the PRISM LED video wall in use). • Double-sided, full colour.

```html
<!DOCTYPE html>
<html lang="en">
<head>
<meta charset="utf-8">
<title>PRISM LED Video Walls – Schools Flyer</title>
<link href="https://fonts.googleapis.com/css2?family=Montserrat:wght@400;500;600;700;800;900&display=swap" rel="stylesheet">
<style>
  :root {
    --page-bg: #d9d9d9;
    --red: #ee4249;
    --red-2: #d8373f;
    --red-3: #b52d34;
    --red-4: #8f2329;
    --dark: #232527;
    --ink: #2b2d30;
    --white: #ffffff;
    --photo-top: #7d7a76;
    --photo-mid: #a8865a;
    --photo-screen: #5cc6e6;
  }
  * { box-sizing: border-box; margin: 0; padding: 0; }
  html, body { width: 1200px; height: 800px; overflow: hidden; }
  body {
    background: var(--page-bg);
    font-family: 'Montserrat', sans-serif;
    position: relative;
  }
  .flyer {
    position: absolute;
    left: 320px; top: 6px;
    width: 560px; height: 788px;
    background: var(--dark);
    overflow: hidden;
    box-shadow: 0 6px 20px rgba(0,0,0,.18);
  }
  .hero-photo {
    position: absolute; left: 0; top: 0;
    width: 560px; height: 340px;
    background:
      linear-gradient(160deg, transparent 40%, rgba(92,198,230,.85) 41%, rgba(120,210,238,.9) 70%, transparent 71%),
      linear-gradient(180deg, var(--photo-top) 0%, #8e8275 45%, var(--photo-mid) 100%);
  }
  .headline {
    position: absolute; left: 46px; top: 176px;
    width: 300px; height: 178px;
    background: linear-gradient(180deg, #f0474e, var(--red-2));
    color: var(--white);
    font-weight: 900;
    text-transform: uppercase;
    padding: 16px 0 0 18px;
    line-height: 1;
  }
  .headline::before {
    content: ""; position: absolute; left: 0; right: 0; top: -5px; height: 6px;
    background: radial-gradient(circle at 4px 0, transparent 3px, #f0474e 3.5px) 0 0 / 8px 6px repeat-x;
  }
  .headline .line { display: block; font-size: 32px; letter-spacing: .5px; }
  .headline .line.big { font-size: 37px; }
  .year-pill {
    display: inline-block;
    background: var(--dark);
    border-radius: 20px;
    padding: 4px 14px 5px;
    margin: 2px 0 2px 56px;
    font-size: 12px; font-weight: 700;
  }
  .year-pill b { color: var(--red); font-size: 22px; font-weight: 800; margin: 0 4px; }
  .why-title {
    position: absolute; left: 0; width: 560px; top: 364px;
    text-align: center; color: var(--white);
    font-size: 20px; font-weight: 800; letter-spacing: .5px;
  }
  .features {
    position: absolute; left: 30px; top: 402px;
    display: flex; width: 500px; height: 112px;
  }
  .feature {
    flex: 1; position: relative; color: var(--white);
    display: flex; flex-direction: column; align-items: center; justify-content: center;
    text-align: center; font-size: 11px; font-weight: 500; line-height: 1.25; gap: 8px;
  }
  .feature::before {
    content: ""; position: absolute; top: -7px; left: 50%; margin-left: -7px;
    border-left: 7px solid transparent; border-right: 7px solid transparent;
    border-bottom: 7px solid var(--tone);
  }
  .feature { background: var(--tone); }
  .feature.f1 { --tone: var(--red); }
  .feature.f2 { --tone: var(--red-2); }
  .feature.f3 { --tone: var(--red-3); }
  .feature.f4 { --tone: var(--red-4); }
  .feature svg { width: 26px; height: 26px; }
  .benefits {
    position: absolute; left: 40px; top: 540px; width: 220px; color: var(--white);
  }
  .benefits h2 { font-size: 22px; font-weight: 800; margin-bottom: 6px; }
  .benefits p { font-size: 8.5px; line-height: 1.6; }
  .benefits em { color: var(--red); font-style: normal; font-weight: 700; }
  .cta {
    position: absolute; right: 36px; top: 536px; width: 250px;
    color: var(--white); text-align: center; line-height: 1.1;
  }
  .cta .l1 { font-size: 22px; font-weight: 600; }
  .cta .free { color: var(--red); font-size: 34px; font-weight: 900; }
  .cta .l2 { font-size: 20px; font-weight: 500; }
  .cta .l2 b { font-weight: 700; }
  .cta .l3 { font-size: 24px; font-weight: 800; }
  .footer {
    position: absolute; left: 0; bottom: 0; width: 560px; height: 96px;
    background: var(--white);
    display: flex; align-items: center; justify-content: space-between;
    padding: 0 30px 0 36px;
  }
  .brand { display: flex; align-items: center; gap: 10px; color: var(--ink); font-weight: 800; font-size: 30px; letter-spacing: 1px; }
  .brand .dot { width: 14px; height: 14px; background: var(--red); }
  .brand small { font-size: 30px; }
  .contact { color: var(--ink); text-align: right; }
  .contact h3 { font-size: 11px; font-weight: 700; text-align: left; }
  .contact .sites { font-size: 8px; margin: 2px 0 6px; text-align: left; }
  .contact .web { font-size: 15px; font-weight: 800; }
</style>
</head>
<body>
  <main class="flyer">
    <div class="hero-photo" role="img" aria-label="School hall with a large LED video wall showing a snowboarder on a blue snow slope"></div>

    <h1 class="headline">
      <span class="line">Transform</span>
      <span class="line">Your School</span>
      <span class="year-pill">FOR <b>2026</b> WITH</span>
      <span class="line big">PRISM LED</span>
      <span class="line">Video Walls!</span>
    </h1>

    <h2 class="why-title">WHY CHOOSE PRISM</h2>

    <section class="features">
      <div class="feature f1">
        <svg viewBox="0 0 24 24" fill="none" stroke="#fff" stroke-width="1.6"><path d="M12 22s7-7.5 7-12.5A7 7 0 0 0 5 9.5C5 14.5 12 22 12 22z"/><circle cx="12" cy="9.5" r="2.6"/></svg>
        <span>Over 2500+ Video<br>Walls Installed</span>
      </div>
      <div class="feature f2">
        <svg viewBox="0 0 24 24" fill="none" stroke="#fff" stroke-width="1.6"><path d="M4 14v-2a8 8 0 0 1 16 0v2"/><rect x="3" y="13" width="4" height="6" rx="1.5"/><rect x="17" y="13" width="4" height="6" rx="1.5"/><path d="M19 19c0 2-2 3-5 3"/></svg>
        <span>Ongoing Service<br>&amp; Support</span>
      </div>
      <div class="feature f3">
        <svg viewBox="0 0 24 24" fill="none" stroke="#fff" stroke-width="1.6"><circle cx="10" cy="10" r="3"/><path d="M10 3v2M10 15v2M3 10h2M15 10h2M5 5l1.4 1.4M13.6 13.6 15 15M5 15l1.4-1.4M13.6 6.4 15 5"/><path d="M14 16l5 5 2-2-5-5"/></svg>
        <span>Australia-Wide<br>Installation</span>
      </div>
      <div class="feature f4">
        <svg viewBox="0 0 24 24" fill="none" stroke="#fff" stroke-width="1.6"><circle cx="12" cy="12" r="9"/><path d="M15 9c-.5-1-1.6-1.5-3-1.5-1.7 0-3 .8-3 2s1.3 1.7 3 2 3 .8 3 2-1.3 2-3 2c-1.4 0-2.5-.5-3-1.5M12 6v12"/></svg>
        <span>Financing<br>Options</span>
      </div>
    </section>

    <section class="benefits">
      <h2>BENEFITS</h2>
      <p><em>Engaging</em>, high-resolution displays for assemblies, lessons, &amp; events.<br>
      <em>Easy-to-use</em> and fully supported by Lumen AV Group.<br>
      <em>Designed</em> for Education.<br>
      <em>Start 2026</em> with this stunning video display at your school.</p>
    </section>

    <section class="cta">
      <div class="l1">Book Your <span class="free">FREE</span></div>
      <div class="l2">On-Site <b>Demonstration</b></div>
      <div class="l3">Today!</div>
    </section>

    <footer class="footer">
      <div class="brand"><span class="dot"></span>PRISM</div>
      <div class="contact">
        <h3>LOCATION:</h3>
        <p class="sites">Lumen AV Group | Melbourne | Sydney | Perth | Brisbane</p>
        <p class="web">www.tornelascreens.com.au</p>
      </div>
    </footer>
  </main>
</body>
</html>
```